Tech Company requires UI design for mobile app

We need a mobile app design for a company based in Singapore called "Kalvor Systems". We develop innovative Android/iOS business applications. KalvorLink - a collaboration tool targeted at SMEs that improves reporting and communication between different departments of an organisation. We would like to see designs that use the colour orange, our corporate colour. The final design should communicate clean and technology inclined design.

You are expected to recreate the icons, layout and structure without affecting the workflow.This is a workplace app for employee on mobile. The mobile app aims to empower individual employee to complete the following processes:

1. HR processes - taking attendance, timesheet, employment management to payslip)
2. Inventory management - stock taking, gift redemption and real-time stock management
3. Digital form - application for inspection, safety, procurement or request creation)
4. Job - an app that allows web portal to assign work to individual worker.
Updates

Reason: Received feedback to extens timeline. Cheers!

Target Market(s)

C-Executive, office employee, retail promoter, worker

Industry/Entity Type

Business

Colors

Designer to choose colors to be used in the design.

Requirements
Must have
• - Design must be neat, looks professional and perceived to be user-friendly
• - Use colour theme for each category
• - Must complement with KalvorLink logo them (already attached)
• - Have "apple" feel
• - We like the layout reference 1 & reference 2 photo. However, we prefer a better colour theme (Already Attached)
• - Please download the link for the work required
• https://files.quillbox.example/open?id=7Hq2LmPzXw9RtNc4VbKjYs8DfGaTe3Uo
Nice to have
• More info to follow shortly
Should not have
• - Must not be loud, flashy, dull, bored,
• - Design should not clash with Kalvor Link Logo
• -

```html
<!DOCTYPE html>
<html lang="en">
<head>
<meta charset="utf-8">
<title>Kalvor Link — Home Screen Versions</title>
<link href="https://fonts.googleapis.com/css2?family=Open+Sans:wght@300;400;600;700&display=swap" rel="stylesheet">
<style>
:root{
  --bg-top:#1c3246;
  --bg-bottom:#0c1823;
  --orange:#f05a22;
  --orange-light:#f47a2a;
  --ink:#3b3b3b;
  --muted:#8a8a8a;
  --line:#e6e6e6;
  --white:#ffffff;
}
*{box-sizing:border-box;margin:0;padding:0}
html,body{width:1200px;height:990px;overflow:hidden}
body{
  font-family:"Open Sans",Arial,sans-serif;
  background:radial-gradient(ellipse at 60% 10%,var(--bg-top),var(--bg-bottom) 80%);
  position:relative;color:var(--white);
}
.section-title{position:absolute;font-weight:300;font-size:19px;letter-spacing:.2px}
.phone{position:absolute;width:192px;background:var(--white);overflow:hidden;color:var(--ink)}
.phone.v1{height:500px}
.phone.v2,.phone.v3{height:340px}
.header{position:absolute;left:0;top:0;width:100%;height:54px;background:linear-gradient(180deg,var(--orange),var(--orange-light))}
.v3 .header{height:103px}
.status{position:absolute;top:2px;left:0;width:100%;font-size:5.5px;color:var(--white);text-align:center}
.status .sig{position:absolute;left:4px}
.status .bat{position:absolute;right:4px}
.brand{position:absolute;left:8px;top:15px;font-size:8.5px;color:var(--white);display:flex;align-items:center;gap:3px}
.brand i{width:5px;height:5px;background:var(--white);display:block}
.top-icons{position:absolute;right:7px;top:14px;display:flex;gap:9px;color:var(--white)}
.top-icons svg{width:12px;height:12px}
.avatar{position:absolute;left:10px;top:34px;width:37px;height:37px;border-radius:50%;border:1.5px solid var(--white);background:radial-gradient(circle at 50% 40%,#8c8f93,#3a3d42)}
.v3 .avatar{top:38px}
.name{position:absolute;left:55px;top:39px;font-size:9.5px;font-weight:600;color:var(--white)}
.emp{position:absolute;left:55px;top:55px;font-size:8.5px;color:var(--ink)}
.v3 .name{top:44px}
.v3 .emp{top:57px;color:var(--white)}
.tabs{position:absolute;left:10px;top:88px;display:flex;gap:10px;font-size:8.5px;white-space:nowrap;color:#444}
.tabs span{padding-bottom:3px}
.v2 .tabs .on{color:var(--orange);border-bottom:1px solid var(--orange)}
.v3 .tabs{color:rgba(255,255,255,.7)}
.v3 .tabs span{padding-bottom:5px}
.v3 .tabs .on{color:var(--white);font-weight:600;border-bottom:2px solid var(--white)}
.tabs.shift{left:-94px}
.cell{position:absolute;width:90px;text-align:center;font-size:7.5px;color:#555}
.cell svg{width:22px;height:22px;display:block;margin:0 auto 7px;color:#3a3a3a}
.cell.big{font-size:9px}
.v1-head{position:absolute;left:10px;font-size:8.5px;color:var(--ink)}
.v1-rule{position:absolute;left:0;width:100%;height:1px;background:var(--line)}
.mini{position:absolute;width:44px;text-align:center;font-size:6.2px;line-height:1.3;color:#555}
.mini svg{width:16px;height:16px;display:block;margin:0 auto 3px;color:#3a3a3a}
.nav{position:absolute;left:0;bottom:0;width:100%;height:25px;display:flex;background:var(--orange);color:rgba(255,255,255,.8)}
.nav div{flex:1;text-align:center;font-size:4.8px;padding-top:3px}
.nav svg{width:12px;height:12px;display:block;margin:0 auto 1px}
.v1 .nav{height:26px}
.v3 .nav{background:var(--white);border-top:1px solid var(--line);color:#555}
.v3 .nav .on{color:var(--orange)}
.acc{color:var(--orange)}
.footer-brand{position:absolute;left:26px;top:922px;display:flex;align-items:center;gap:10px;font-size:34px;font-weight:400;color:var(--white)}
.footer-brand i{width:14px;height:14px;background:var(--orange);display:block}
</style>
</head>
<body>
<svg width="0" height="0" style="position:absolute">
  <defs>
    <symbol id="i-user" viewBox="0 0 24 24"><g fill="none" stroke="currentColor" stroke-width="1.4"><circle cx="11" cy="8" r="4.5"/><path d="M3 21c0-4.5 3.5-7.5 8-7.5 1.5 0 2.8.3 3.8.9"/></g><path d="M15 18l2 2 4-4" fill="none" stroke="#f05a22" stroke-width="1.4"/></symbol>
    <symbol id="i-today" viewBox="0 0 24 24"><g fill="none" stroke="currentColor" stroke-width="1.4"><rect x="3" y="4" width="18" height="17" rx="2"/><path d="M8 2v4M16 2v4"/></g><g fill="currentColor"><circle cx="8" cy="11" r="1"/><circle cx="12" cy="11" r="1"/><circle cx="16" cy="11" r="1"/><circle cx="8" cy="16" r="1"/><circle cx="12" cy="16" r="1"/><circle cx="16" cy="16" r="1"/></g></symbol>
    <symbol id="i-folder" viewBox="0 0 24 24"><path d="M2 7h7l2 2h10v11H2z" fill="none" stroke="currentColor" stroke-width="1.4"/><circle cx="16" cy="16" r="3.5" fill="#fff" stroke="#f05a22" stroke-width="1.3"/><path d="M16 14.5V16h1.3" fill="none" stroke="#f05a22" stroke-width="1.2"/></symbol>
    <symbol id="i-pin" viewBox="0 0 24 24"><path d="M12 3a5 5 0 0 1 5 5c0 4-5 9-5 9s-5-5-5-9a5 5 0 0 1 5-5z" fill="none" stroke="currentColor" stroke-width="1.4"/><circle cx="12" cy="8" r="1.8" fill="none" stroke="#f05a22" stroke-width="1.3"/><path d="M3 21l4-6h10l4 6z" fill="none" stroke="currentColor" stroke-width="1.4"/></symbol>
    <symbol id="i-gift" viewBox="0 0 24 24"><g fill="none" stroke="currentColor" stroke-width="1.4"><rect x="3" y="8" width="18" height="4"/><rect x="4.5" y="12" width="15" height="9"/><path d="M12 8v13"/></g><path d="M12 8c-2-4-6-4-5-1 .5 1 3 1 5 1zm0 0c2-4 6-4 5-1-.5 1-3 1-5 1z" fill="none" stroke="#f05a22" stroke-width="1.3"/></symbol>
    <symbol id="i-eye" viewBox="0 0 24 24"><path d="M2 12s4-6 10-6 10 6 10 6-4 6-10 6S2 12 2 12z" fill="none" stroke="currentColor" stroke-width="1.4"/><circle cx="12" cy="12" r="3" fill="none" stroke="#f05a22" stroke-width="1.4"/></symbol>
    <symbol id="i-camera" viewBox="0 0 24 24"><path d="M3 8h4l2-2h6l2 2h4v12H3z" fill="none" stroke="currentColor" stroke-width="1.4"/><circle cx="12" cy="13.5" r="3.5" fill="none" stroke="#f05a22" stroke-width="1.4"/></symbol>
    <symbol id="i-chart" viewBox="0 0 24 24"><g fill="none" stroke="currentColor" stroke-width="1.4"><rect x="2" y="4" width="20" height="13"/><path d="M12 17v3M8 21h8"/></g><path d="M5 14l4-4 3 2 6-5" fill="none" stroke="#f05a22" stroke-width="1.3"/></symbol>
    <symbol id="i-clip" viewBox="0 0 24 24"><g fill="none" stroke="currentColor" stroke-width="1.4"><rect x="4" y="4" width="15" height="18"/><rect x="8" y="2" width="7" height="3"/><path d="M7 9h9M7 12h9M7 15h6"/></g><path d="M14 19l2 2 4-4" fill="none" stroke="#f05a22" stroke-width="1.4"/></symbol>
    <symbol id="i-truck" viewBox="0 0 24 24"><g fill="none" stroke="currentColor" stroke-width="1.4"><path d="M5 7h11v10H5zM16 10h4l2 3v4h-6"/><circle cx="8" cy="18" r="1.8"/><circle cx="18" cy="18" r="1.8"/></g><path d="M1 9h3M1 12h3M2 15h2" stroke="#f05a22" stroke-width="1.3"/></symbol>
    <symbol id="i-basket" viewBox="0 0 24 24"><path d="M4 5h16l-2 16H6z" fill="none" stroke="currentColor" stroke-width="1.4"/><path d="M9 10c0 3 6 3 6 0" fill="none" stroke="#f05a22" stroke-width="1.4"/></symbol>
    <symbol id="i-doc" viewBox="0 0 24 24"><path d="M5 2h10l4 4v16H5z" fill="none" stroke="currentColor" stroke-width="1.4"/><path d="M8 11h8M8 14h8M8 17h8" stroke="#f05a22" stroke-width="1.3"/></symbol>
    <symbol id="i-cal" viewBox="0 0 24 24"><g fill="none" stroke="currentColor" stroke-width="1.4"><rect x="3" y="4" width="18" height="16" rx="1"/><path d="M3 9h18M8 2v4M16 2v4M6 14h7M10 11.5l3 2.5-3 2.5"/></g></symbol>
    <symbol id="i-forms" viewBox="0 0 24 24"><g fill="none" stroke="currentColor" stroke-width="1.4"><path d="M8 2h8l3 3v13H8z"/><path d="M5 6v16h11"/></g><path d="M11 10h5M11 13h5" stroke="#f05a22" stroke-width="1.3"/></symbol>
    <symbol id="i-job" viewBox="0 0 24 24"><g fill="none" stroke="currentColor" stroke-width="1.4"><rect x="3" y="7" width="18" height="14"/><path d="M9 7V4h6v3M3 12h18"/></g><rect x="10.5" y="10.5" width="3" height="3" fill="#f05a22"/></symbol>
    <symbol id="n-grid" viewBox="0 0 24 24"><g fill="none" stroke="currentColor" stroke-width="1.5"><rect x="3" y="3" width="7" height="7"/><rect x="14" y="3" width="7" height="7"/><rect x="3" y="14" width="7" height="7"/><rect x="14" y="14" width="7" height="7"/></g></symbol>
    <symbol id="n-cal" viewBox="0 0 24 24"><g fill="none" stroke="currentColor" stroke-width="1.5"><rect x="3" y="4" width="18" height="17" rx="2"/><path d="M3 9h18M8 13h2M12 13h2M16 13h2M8 17h2M12 17h2"/></g></symbol>
    <symbol id="n-sync" viewBox="0 0 24 24"><g fill="none" stroke="currentColor" stroke-width="1.5"><path d="M19 12a7 7 0 0 1-12 5M5 12a7 7 0 0 1 12-5"/><path d="M17 3v4h-4M7 21v-4h4"/></g></symbol>
    <symbol id="n-user" viewBox="0 0 24 24"><g fill="none" stroke="currentColor" stroke-width="1.5"><circle cx="12" cy="8" r="4.5"/><path d="M3 21c0-5 4-8 9-8s9 3 9 8z"/></g></symbol>
    <symbol id="t-bell" viewBox="0 0 24 24"><path d="M6 17l2-9a4 4 0 0 1 8 0l2 9zM10 20h4" fill="none" stroke="currentColor" stroke-width="1.6" transform="rotate(-15 12 12)"/></symbol>
    <symbol id="t-gear" viewBox="0 0 24 24"><g fill="none" stroke="currentColor" stroke-width="1.6"><circle cx="12" cy="12" r="3.5"/><path d="M12 2v3M12 19v3M2 12h3M19 12h3M5 5l2 2M17 17l2 2M5 19l2-2M17 7l2-2"/><circle cx="12" cy="12" r="7"/></g></symbol>
  </defs>
</svg>

<h2 class="section-title" style="left:14px;top:42px">Home Screen Version 1</h2>
<h2 class="section-title" style="left:604px;top:42px">Home Screen Version 2</h2>
<h2 class="section-title" style="left:604px;top:476px">Home Screen Version 3</h2>

<!-- Version 1: full dashboard -->
<div class="phone v1" style="left:13px;top:92px">
  <div class="header"></div>
  <div class="status"><span class="sig">●●● ◠</span>9:41 AM<span class="bat">100% ▬</span></div>
  <div class="brand"><i></i>Kalvor</div>
  <div class="top-icons"><svg><use href="#t-bell"/></svg><svg><use href="#t-gear"/></svg></div>
  <div class="avatar" role="img" aria-label="Employee profile photo"></div>
  <div class="name">Daniel Ashford</div>
  <div class="emp">EM1104</div>

  <div class="v1-head" style="top:86px">Attendance</div>
  <div class="mini" style="left:8px;top:104px"><svg><use href="#i-user"/></svg>Take<br>Attendance</div>
  <div class="mini" style="left:52px;top:104px"><svg><use href="#i-today"/></svg>Today</div>
  <div class="mini" style="left:95px;top:104px"><svg><use href="#i-folder"/></svg>Past<br>Records</div>
  <div class="mini" style="left:138px;top:104px"><svg><use href="#i-pin"/></svg>Station</div>
  <div class="v1-rule" style="top:154px"></div>

  <div class="v1-head" style="top:166px">Sales</div>
  <div class="mini" style="left:8px;top:184px"><svg><use href="#i-gift"/></svg>New<br>Redemption</div>
  <div class="mini" style="left:52px;top:184px"><svg><use href="#i-eye"/></svg>View<br>Redemptions</div>
  <div class="mini" style="left:95px;top:184px"><svg><use href="#i-camera"/></svg>Take<br>Photo</div>
  <div class="mini" style="left:138px;top:184px"><svg><use href="#i-chart"/></svg>Sales<br>Summary</div>
  <div class="v1-rule" style="top:234px"></div>

  <div class="v1-head" style="top:246px">Inventory</div>
  <div class="mini" style="left:8px;top:264px"><svg><use href="#i-clip"/></svg>Inventory<br>Check</div>
  <div class="mini" style="left:52px;top:264px"><svg><use href="#i-truck"/></svg>Delivery</div>
  <div class="mini" style="left:95px;top:264px"><svg><use href="#i-basket"/></svg>New<br>Stock Take</div>
  <div class="mini" style="left:138px;top:264px"><svg><use href="#i-doc"/></svg>Stock<br>Take List</div>
  <div class="v1-rule" style="top:314px"></div>

  <div class="v1-head" style="top:326px">Leave</div>
  <div class="mini" style="left:8px;top:344px"><svg><use href="#i-cal"/></svg>Apply<br>Leave</div>
  <div class="mini" style="left:52px;top:344px"><svg><use href="#i-cal"/></svg>Leave<br>Status</div>
  <div class="mini" style="left:95px;top:344px"><svg><use href="#i-cal"/></svg>Balance</div>
  <div class="mini" style="left:138px;top:344px"><svg><use href="#i-cal"/></svg>Pending<br>Action</div>
  <div class="v1-rule" style="top:394px"></div>

  <div class="v1-head" style="top:406px">Workforce Management</div>
  <div class="mini" style="left:8px;top:424px"><svg><use href="#i-forms"/></svg>Forms</div>
  <div class="mini" style="left:52px;top:424px"><svg><use href="#i-job"/></svg>My Job</div>

  <nav class="nav"><div><svg><use href="#n-grid"/></svg>Dashboard</div><div><svg><use href="#n-cal"/></svg>Calendar</div><div><svg><use href="#n-sync"/></svg>Sync</div><div><svg><use href="#n-user"/></svg>Profile</div></nav>
</div>

<!-- Version 2: tabbed, white tabs -->
<div class="phone v2" style="left:209px;top:92px">
  <div class="header"></div>
  <div class="status"><span class="sig">●●● ◠</span>9:41 AM<span class="bat">100% ▬</span></div>
  <div class="brand"><i></i>Kalvor</div>
  <div class="top-icons"><svg><use href="#t-bell"/></svg><svg><use href="#t-gear"/></svg></div>
  <div class="avatar" role="img" aria-label="Employee profile photo"></div>
  <div class="name">Daniel Ashford</div><div class="emp">EM1104</div>
  <div class="tabs"><span class="on">Attendance</span><span>Sales</span><span>Inventory</span><span>Leave</span><span>Workforce Management</span></div>
  <div class="cell" style="left:10px;top:137px"><svg><use href="#i-user"/></svg>Take Attendance</div>
  <div class="cell" style="left:92px;top:137px"><svg><use href="#i-today"/></svg>Today</div>
  <div class="cell" style="left:10px;top:216px"><svg><use href="#i-folder"/></svg>Past Records</div>
  <div class="cell" style="left:92px;top:216px"><svg><use href="#i-pin"/></svg>Station</div>
  <nav class="nav"><div><svg><use href="#n-grid"/></svg>Dashboard</div><div><svg><use href="#n-cal"/></svg>Calendar</div><div><svg><use href="#n-sync"/></svg>Sync</div><div><svg><use href="#n-user"/></svg>Profile</div></nav>
</div>

<div class="phone v2" style="left:406px;top:92px">
  <div class="header"></div>
  <div class="status"><span class="sig">●●● ◠</span>9:41 AM<span class="bat">100% ▬</span></div>
  <div class="brand"><i></i>Kalvor</div>
  <div class="top-icons"><svg><use href="#t-bell"/></svg><svg><use href="#t-gear"/></svg></div>
  <div class="avatar" role="img" aria-label="Employee profile photo"></div>
  <div class="name">Daniel Ashford</div><div class="emp">EM1104</div>
  <div class="tabs"><span>Attendance</span><span class="on">Sales</span><span>Inventory</span><span>Leave</span><span>Workforce Management</span></div>
  <div class="cell" style="left:10px;top:137px"><svg><use href="#i-gift"/></svg>New Redemption</div>
  <div class="cell" style="left:92px;top:137px"><svg><use href="#i-eye"/></svg>View Redemptions</div>
  <div class="cell" style="left:10px;top:216px"><svg><use href="#i-camera"/></svg>Take Photo</div>
  <div class="cell" style="left:92px;top:216px"><svg><use href="#i-chart"/></svg>Sales Summary</div>
  <nav class="nav"><div><svg><use href="#n-grid"/></svg>Dashboard</div><div><svg><use href="#n-cal"/></svg>Calendar</div><div><svg><use href="#n-sync"/></svg>Sync</div><div><svg><use href="#n-user"/></svg>Profile</div></nav>
</div>

<div class="phone v2" style="left:602px;top:92px">
  <div class="header"></div>
  <div class="status"><span class="sig">●●● ◠</span>9:41 AM<span class="bat">100% ▬</span></div>
  <div class="brand"><i></i>Kalvor</div>
  <div class="top-icons"><svg><use href="#t-bell"/></svg><svg><use href="#t-gear"/></svg></div>
  <div class="avatar" role="img" aria-label="Employee profile photo"></div>
  <div class="name">Daniel Ashford</div><div class="emp">EM1104</div>
  <div class="tabs"><span>Attendance</span><span>Sales</span><span class="on">Inventory</span><span>Leave</span><span>Workforce Management</span></div>
  <div class="cell" style="left:10px;top:137px"><svg><use href="#i-clip"/></svg>Inventory Check</div>
  <div class="cell" style="left:92px;top:137px"><svg><use href="#i-truck"/></svg>Delivery</div>
  <div class="cell" style="left:10px;top:216px"><svg><use href="#i-basket"/></svg>New Stock Take</div>
  <div class="cell" style="left:92px;top:216px"><svg><use href="#i-doc"/></svg>Stock Take List</div>
  <nav class="nav"><div><svg><use href="#n-grid"/></svg>Dashboard</div><div><svg><use href="#n-cal"/></svg>Calendar</div><div><svg><use href="#n-sync"/></svg>Sync</div><div><svg><use href="#n-user"/></svg>Profile</div></nav>
</div>

<div class="phone v2" style="left:799px;top:92px">
  <div class="header"></div>
  <div class="status"><span class="sig">●●● ◠</span>9:41 AM<span class="bat">100% ▬</span></div>
  <div class="brand"><i></i>Kalvor</div>
  <div class="top-icons"><svg><use href="#t-bell"/></svg><svg><use href="#t-gear"/></svg></div>
  <div class="avatar" role="img" aria-label="Employee profile photo"></div>
  <div class="name">Daniel Ashford</div><div class="emp">EM1104</div>
  <div class="tabs"><span>Attendance</span><span>Sales</span><span>Inventory</span><span class="on">Leave</span><span>Workforce Management</span></div>
  <div class="cell" style="left:10px;top:137px"><svg><use href="#i-cal"/></svg>Apply Leave</div>
  <div class="cell" style="left:92px;top:137px"><svg><use href="#i-cal"/></svg>Leave Status</div>
  <div class="cell" style="left:10px;top:216px"><svg><use href="#i-cal"/></svg>Balance</div>
  <div class="cell" style="left:92px;top:216px"><svg><use href="#i-cal"/></svg>Pending Action</div>
  <nav class="nav"><div><svg><use href="#n-grid"/></svg>Dashboard</div><div><svg><use href="#n-cal"/></svg>Calendar</div><div><svg><use href="#n-sync"/></svg>Sync</div><div><svg><use href="#n-user"/></svg>Profile</div></nav>
</div>

<div class="phone v2" style="left:996px;top:92px">
  <div class="header"></div>
  <div class="status"><span class="sig">●●● ◠</span>9:41 AM<span class="bat">100% ▬</span></div>
  <div class="brand"><i></i>Kalvor</div>
  <div class="top-icons"><svg><use href="#t-bell"/></svg><svg><use href="#t-gear"/></svg></div>
  <div class="avatar" role="img" aria-label="Employee profile photo"></div>
  <div class="name">Daniel Ashford</div><div class="emp">EM1104</div>
  <div class="tabs shift"><span>Attendance</span><span>Sales</span><span>Inventory</span><span>Leave</span><span class="on">Workforce Management</span></div>
  <div class="cell big" style="left:10px;top:137px"><svg><use href="#i-forms"/></svg>Forms</div>
  <div class="cell" style="left:92px;top:137px"><svg><use href="#i-job"/></svg>My Job</div>
  <nav class="nav"><div><svg><use href="#n-grid"/></svg>Dashboard</div><div><svg><use href="#n-cal"/></svg>Calendar</div><div><svg><use href="#n-sync"/></svg>Sync</div><div><svg><use href="#n-user"/></svg>Profile</div></nav>
</div>

<!-- Version 3: tabs inside orange header -->
<div class="phone v3" style="left:209px;top:526px">
  <div class="header"></div>
  <div class="status"><span class="sig">●●● ◠</span>9:41 AM<span class="bat">100% ▬</span></div>
  <div class="brand"><i></i>Kalvor</div>
  <div class="top-icons"><svg><use href="#t-bell"/></svg><svg><use href="#t-gear"/></svg></div>
  <div class="avatar" role="img" aria-label="Employee profile photo"></div>
  <div class="name">Daniel Ashford</div><div class="emp">EM1104</div>
  <div class="tabs"><span class="on">Attendance</span><span>Sales</span><span>Inventory</span><span>Leave</span><span>Workforce Management</span></div>
  <div class="cell" style="left:10px;top:142px"><svg><use href="#i-user"/></svg>Take Attendance</div>
  <div class="cell" style="left:92px;top:142px"><svg><use href="#i-today"/></svg>Today</div>
  <div class="cell" style="left:10px;top:222px"><svg><use href="#i-folder"/></svg>Past Records</div>
  <div class="cell" style="left:92px;top:222px"><svg><use href="#i-pin"/></svg>Station</div>
  <nav class="nav"><div class="on"><svg><use href="#n-grid"/></svg>Dashboard</div><div><svg><use href="#n-cal"/></svg>Calendar</div><div><svg><use href="#n-sync"/></svg>Sync</div><div><svg><use href="#n-user"/></svg>Profile</div></nav>
</div>

<div class="phone v3" style="left:406px;top:526px">
  <div class="header"></div>
  <div class="status"><span class="sig">●●● ◠</span>9:41 AM<span class="bat">100% ▬</span></div>
  <div class="brand"><i></i>Kalvor</div>
  <div class="top-icons"><svg><use href="#t-bell"/></svg><svg><use href="#t-gear"/></svg></div>
  <div class="avatar" role="img" aria-label="Employee profile photo"></div>
  <div class="name">Daniel Ashford</div><div class="emp">EM1104</div>
  <div class="tabs"><span>Attendance</span><span class="on">Sales</span><span>Inventory</span><span>Leave</span><span>Workforce Management</span></div>
  <div class="cell" style="left:10px;top:142px"><svg><use href="#i-gift"/></svg>New Redemption</div>
  <div class="cell" style="left:92px;top:142px"><svg><use href="#i-eye"/></svg>View Redemptions</div>
  <div class="cell" style="left:10px;top:222px"><svg><use href="#i-camera"/></svg>Take Photo</div>
  <div class="cell" style="left:92px;top:222px"><svg><use href="#i-chart"/></svg>Sales Summary</div>
  <nav class="nav"><div class="on"><svg><use href="#n-grid"/></svg>Dashboard</div><div><svg><use href="#n-cal"/></svg>Calendar</div><div><svg><use href="#n-sync"/></svg>Sync</div><div><svg><use href="#n-user"/></svg>Profile</div></nav>
</div>

<div class="phone v3" style="left:602px;top:526px">
  <div class="header"></div>
  <div class="status"><span class="sig">●●● ◠</span>9:41 AM<span class="bat">100% ▬</span></div>
  <div class="brand"><i></i>Kalvor</div>
  <div class="top-icons"><svg><use href="#t-bell"/></svg><svg><use href="#t-gear"/></svg></div>
  <div class="avatar" role="img" aria-label="Employee profile photo"></div>
  <div class="name">Daniel Ashford</div><div class="emp">EM1104</div>
  <div class="tabs"><span>Attendance</span><span>Sales</span><span class="on">Inventory</span><span>Leave</span><span>Workforce Management</span></div>
  <div class="cell" style="left:10px;top:142px"><svg><use href="#i-clip"/></svg>Inventory Check</div>
  <div class="cell" style="left:92px;top:142px"><svg><use href="#i-truck"/></svg>Delivery</div>
  <div class="cell" style="left:10px;top:222px"><svg><use href="#i-basket"/></svg>New Stock Take</div>
  <div class="cell" style="left:92px;top:222px"><svg><use href="#i-doc"/></svg>Stock Take List</div>
  <nav class="nav"><div class="on"><svg><use href="#n-grid"/></svg>Dashboard</div><div><svg><use href="#n-cal"/></svg>Calendar</div><div><svg><use href="#n-sync"/></svg>Sync</div><div><svg><use href="#n-user"/></svg>Profile</div></nav>
</div>

<div class="phone v3" style="left:799px;top:526px">
  <div class="header"></div>
  <div class="status"><span class="sig">●●● ◠</span>9:41 AM<span class="bat">100% ▬</span></div>
  <div class="brand"><i></i>Kalvor</div>
  <div class="top-icons"><svg><use href="#t-bell"/></svg><svg><use href="#t-gear"/></svg></div>
  <div class="avatar" role="img" aria-label="Employee profile photo"></div>
  <div class="name">Daniel Ashford</div><div class="emp">EM1104</div>
  <div class="tabs"><span>Attendance</span><span>Sales</span><span>Inventory</span><span class="on">Leave</span><span>Workforce Management</span></div>
  <div class="cell" style="left:10px;top:142px"><svg><use href="#i-cal"/></svg>Apply Leave</div>
  <div class="cell" style="left:92px;top:142px"><svg><use href="#i-cal"/></svg>Leave Status</div>
  <div class="cell" style="left:10px;top:222px"><svg><use href="#i-cal"/></svg>Balance</div>
  <div class="cell" style="left:92px;top:222px"><svg><use href="#i-cal"/></svg>Pending Action</div>
  <nav class="nav"><div class="on"><svg><use href="#n-grid"/></svg>Dashboard</div><div><svg><use href="#n-cal"/></svg>Calendar</div><div><svg><use href="#n-sync"/></svg>Sync</div><div><svg><use href="#n-user"/></svg>Profile</div></nav>
</div>

<div class="phone v3" style="left:996px;top:526px">
  <div class="header"></div>
  <div class="status"><span class="sig">●●● ◠</span>9:41 AM<span class="bat">100% ▬</span></div>
  <div class="brand"><i></i>Kalvor</div>
  <div class="top-icons"><svg><use href="#t-bell"/></svg><svg><use href="#t-gear"/></svg></div>
  <div class="avatar" role="img" aria-label="Employee profile photo"></div>
  <div class="name">Daniel Ashford</div><div class="emp">EM1104</div>
  <div class="tabs shift"><span>Attendance</span><span>Sales</span><span>Inventory</span><span>Leave</span><span class="on">Workforce Management</span></div>
  <div class="cell big" style="left:10px;top:142px"><svg><use href="#i-forms"/></svg>Forms</div>
  <div class="cell" style="left:92px;top:142px"><svg><use href="#i-job"/></svg>My Job</div>
  <nav class="nav"><div class="on"><svg><use href="#n-grid"/></svg>Dashboard</div><div><svg><use href="#n-cal"/></svg>Calendar</div><div><svg><use href="#n-sync"/></svg>Sync</div><div><svg><use href="#n-user"/></svg>Profile</div></nav>
</div>

<div class="footer-brand"><i></i>Kalvor</div>
</body>
</html>
```